Redesign Colorful Business Card

Please redesign the card attached. It is too busy. Please don't eliminate any of the words. The repetivite word "free" can be used less often.

Target Market(s)

College Students.

Contact Information for Business Card

The details listed in the attached image

Font styles to use
Sans Serif

Requirements
Must have
• A clear and simple presentation and must be attractive.

```html
<!DOCTYPE html>
<html lang="en">
<head>
<meta charset="UTF-8">
<title>StudyNimble Card</title>
<link href="https://fonts.googleapis.com/css2?family=Arimo:wght@700&family=Share+Tech+Mono&display=swap" rel="stylesheet">
<style>
  :root {
    --card-blue: #1b4894;
    --sky: #8ecff3;
    --white: #ffffff;
    --ink: #111111;
    --accent-yellow: #f3dc1d;
    --page: #ffffff;
  }
  * { margin: 0; padding: 0; box-sizing: border-box; }
  html, body {
    width: 1200px;
    height: 686px;
    overflow: hidden;
    background: var(--page);
  }
  .card {
    position: relative;
    width: 1200px;
    height: 686px;
    background: var(--card-blue);
    border-radius: 30px;
    font-family: 'Arimo', Arial, sans-serif;
    font-weight: 700;
    color: var(--white);
  }
  .benefit {
    position: absolute;
    font-size: 34px;
    line-height: 44px;
  }
  .benefit--left { left: 126px; top: 90px; }
  .benefit--right { right: 126px; top: 90px; text-align: right; }
  .benefit--center { left: 0; width: 1200px; top: 267px; text-align: center; }
  .timeline {
    position: absolute;
    left: 205px;
    top: 190px;
  }
  .brand {
    position: absolute;
    left: 72px;
    top: 546px;
    display: flex;
    align-items: center;
    gap: 22px;
  }
  .brand__dot {
    width: 62px;
    height: 62px;
    border-radius: 50%;
    background: var(--sky);
  }
  .brand__name {
    font-size: 42px;
    line-height: 1;
    color: var(--white);
    text-decoration: underline;
    text-decoration-thickness: 3px;
    text-underline-offset: 5px;
  }
  .free-badge {
    position: absolute;
    left: 910px;
    top: 404px;
    width: 168px;
    height: 108px;
    background: var(--sky);
    border: 2px solid var(--accent-yellow);
    border-radius: 16px;
    transform: rotate(-3deg);
    display: flex;
    align-items: center;
    justify-content: center;
    font-family: 'Share Tech Mono', monospace;
    font-size: 52px;
    letter-spacing: 6px;
    color: var(--ink);
  }
  .megaphone {
    position: absolute;
    left: 868px;
    top: 536px;
    width: 88px;
    height: 92px;
    border-radius: 14px;
    background: linear-gradient(135deg, var(--white), var(--accent-yellow));
  }
</style>
</head>
<body>
  <div class="card">
    <p class="benefit benefit--left">Cut Study Time<br>Down By Up To 50%</p>
    <p class="benefit benefit--right">Memorize Anything<br>Quickly</p>

    <svg class="timeline" width="790" height="56" viewBox="0 0 790 56" aria-hidden="true">
      <rect x="4" y="16" width="782" height="24" rx="12" fill="var(--white)"/>
      <rect x="10" y="22" width="770" height="12" rx="6" fill="var(--sky)"/>
      <g fill="var(--sky)" stroke="var(--white)" stroke-width="5">
        <circle cx="32" cy="28" r="20"/>
        <circle cx="393" cy="28" r="20"/>
        <circle cx="757" cy="28" r="20"/>
      </g>
    </svg>

    <p class="benefit benefit--center">Learn A Subject<br>Without Having To<br>Go To Class</p>

    <div class="brand">
      <span class="brand__dot" aria-hidden="true"></span>
      <span class="brand__name">StudyNimble.com</span>
    </div>

    <div class="free-badge">FREE</div>
    <div class="megaphone" role="img" aria-label="Megaphone illustration announcing the free offer"></div>
  </div>
</body>
</html>
```